Event Ticketing homepage design

This contest is for an event ticketing homepage to be based on the script - http://www.galvorin-passhub.example/demo5/index.php.

Similar ticketing systems for which ideas can be generated are: tollaquin dotcom, brisemark dotcom and quorvilla dotcom.

The homepage these will be based on this design: http://www.plimvey.example/nl/home.html

Features that the design should have include:

1. All positions shown in the demo
2. Top navigation menu: Left hand side - Brookline and Chirpwell icons, Add event. Right hand side – Sign Up, Sign In, Forgot Password
3. Featured events with “buy now” buttons
4. Search function
5. Brookline connect (near login)
6. Create event (see tollaquin dotcom)
7. Most viewed (see brisemark dotcom)
8. Best sellers (see brisemark dotcom)
9. Main Menu navigation buttons: Home,
10. About us, How to advertise, Policies, How to purchase, Terms and Conditions, FAQs, Privacy Policy, Contact Us, Copyright in the footer
11. Hot spots (see quorvilla dotcom)

I will provide the background image to top designers before choosing a finalist
Final design should have high quality PSD files.
Updates

Reason: Due to request from Lou, i have decided to add 4 more days

Here is the new inspiration http://vardolenworks.example/devpro/DuskHarbor/index.html

Thanks for the designs. We'll be giving feedback to all by the end of today (US eastern time)

Thanks for all designs submitted. As the contest is only one or several designs can be considered and so if I don't leave feedback know that it was not shortlisted to be among the finalists.

Reason: For changes

Industry/Entity Type

Events

```html
<!DOCTYPE html>
<html lang="en">
<head>
<meta charset="utf-8">
<title>Event Ticketing</title>
<link href="https://fonts.googleapis.com/css2?family=Ubuntu:wght@400;500;700&display=swap" rel="stylesheet">
<style>
:root{
  --blue:#1a7fd0;
  --link:#1f86d4;
  --bar-top:#5a5a5a;
  --bar-bottom:#2f2f2f;
  --text:#444;
  --muted:#666;
  --panel-line:#dcdcdc;
  --row-bg:#ececec;
  --footer:#7a7a7a;
}
*{box-sizing:border-box;margin:0;padding:0}
html,body{width:1037px;height:1200px;overflow:hidden}
body{font-family:'Ubuntu',sans-serif;color:var(--text);position:relative;
  background:radial-gradient(ellipse at 15% 70%,#2f7fd8 0%,#0d2c6a 35%,#040a22 70%),#050c24}
.backdrop{position:absolute;inset:0;background:radial-gradient(ellipse at 90% 75%,rgba(60,150,240,.55),transparent 45%),radial-gradient(ellipse at 5% 30%,rgba(40,110,220,.35),transparent 40%)}
.page{position:absolute;left:105px;top:0;width:827px;height:1200px;background:#fff}
.topnav{height:27px;background:linear-gradient(var(--bar-top),var(--bar-bottom));display:flex;align-items:stretch;font-size:11px;color:#eee}
.topnav a{color:#eee;text-decoration:none}
.topnav .tab{padding:0 18px;display:flex;align-items:center;border-right:1px solid #222;font-size:11.5px}
.topnav .tab.active{background:linear-gradient(#2c92e0,#1469b5);font-weight:700}
.topnav .account{margin-left:auto;display:flex;align-items:center;font-size:8.5px;padding-right:3px;gap:3px}
.header{height:86px;background:linear-gradient(#fafafa,#ececec);position:relative;border-bottom:4px solid var(--blue)}
.brand{position:absolute;left:11px;top:28px;font-size:29px;font-weight:500;letter-spacing:1px;color:#555}
.follow{position:absolute;right:9px;top:8px;display:flex;align-items:center;gap:5px;color:#999;font-size:14px}
.sq{width:16px;height:16px;border-radius:3px;background:#4a78b8;display:inline-block}
.sq.alt{background:#5db6e8}
.search{position:absolute;right:65px;top:60px;width:170px;height:21px;border:1px solid #ddd;border-radius:3px;background:#fff;font-size:9px;color:#aaa;padding:5px 4px}
.search-btn{position:absolute;right:8px;top:60px;width:41px;height:21px;border-radius:3px;background:linear-gradient(#2c92e0,#1266b0);color:#fff;font-size:10px;font-weight:700;text-align:center;line-height:21px}
.panel{position:absolute;border:1px solid var(--panel-line);border-radius:5px;background:#fff}
.bar{height:23px;background:linear-gradient(var(--bar-top),var(--bar-bottom));border-radius:5px 5px 0 0;color:#fff;font-size:13px;padding:4px 15px;text-transform:uppercase}
.featured{left:7px;top:131px;width:591px;height:354px}
.frow{position:absolute;left:9px;width:573px;height:71px;border:1px solid #e2e2e2;border-radius:5px;background:linear-gradient(#fafafa,var(--row-bg));font-size:9.5px;color:var(--muted)}
.thumb{position:absolute;border:3px solid #fff;box-shadow:0 0 2px #aaa}
.frow .thumb{left:9px;top:9px;width:110px;height:55px}
.frow .info{position:absolute;left:140px;top:19px;line-height:20px}
.frow .venue{position:absolute;left:344px;top:21px;line-height:15px}
.venue b,.blue{color:var(--link);font-weight:500}
.frow .date{position:absolute;right:12px;top:10px;width:80px;text-align:center;color:#555;line-height:15px;font-weight:500}
.buy{display:inline-flex;align-items:center;gap:5px;height:20px;padding:0 4px 0 8px;border-radius:4px;background:linear-gradient(#2c92e0,#1266b0);color:#fff;font-size:9.5px;font-weight:700}
.buy i{width:11px;height:11px;border-radius:50%;background:#fff;display:inline-block;position:relative}
.buy i:after{content:"";position:absolute;left:4px;top:3px;border-left:4px solid #1a7fd0;border-top:2.5px solid transparent;border-bottom:2.5px solid transparent}
.frow .buy{position:absolute;right:14px;top:43px}
.list{left:7px;top:501px;width:285px;height:272px}
.list.viewed{left:311px;width:287px}
.item{position:absolute;left:9px;right:9px;height:66px;border:1px solid #e2e2e2;border-radius:5px;background:linear-gradient(#fafafa,var(--row-bg));font-size:9.5px;line-height:13.3px;padding:5px 5px;color:#444}
.item .thumb{right:6px;top:5px;width:56px;height:25px;border-width:2px}
.item .buy{position:absolute;right:8px;top:41px}
.create{left:7px;top:784px;width:591px;height:156px}
.arrow{position:absolute;top:42px}
.card{position:absolute;top:40px;width:111px;text-align:center;font-size:9.5px;color:var(--muted);line-height:13px}
.card .shot{height:70px;margin-bottom:9px}
.card b{color:var(--link);font-weight:400;display:block}
.side{left:611px;width:209px}
.sbar{height:28px;background:linear-gradient(#2e95e2,#0e5fae);border-radius:5px 5px 0 0;color:#fff;font-size:13px;display:flex;align-items:center;padding-left:9px;gap:9px}
.sbar .ic{width:22px;height:20px;display:inline-block}
.login{top:127px;height:121px;font-size:9px}
.field{position:absolute;left:11px;font-size:9px;color:#555}
.field span{position:absolute;left:54px;top:-3px;width:136px;height:15px;border:1px solid #ccc}
.forgot{position:absolute;left:11px;top:104px;color:#c00;font-size:9px}
.login-btn{position:absolute;right:8px;top:95px;width:50px;height:19px;border-radius:3px;background:linear-gradient(#777,#333);color:#fff;font-size:9.5px;text-align:center;line-height:19px}
.fb{top:261px;height:195px}
.like{position:absolute;left:6px;top:34px;border:1px solid #bbb;border-radius:2px;font-size:8px;padding:2px 4px;color:#3b5a9a}
.fbname{position:absolute;right:8px;top:33px;font-size:15px;font-weight:700;color:#3b5a9a}
.fbcount{position:absolute;left:12px;top:55px;font-size:10.5px;color:#222}
.faces{position:absolute;left:10px;top:72px;display:grid;grid-template-columns:repeat(4,41px);gap:4px 5px}
.faces span{height:41px;display:block}
.plugin{position:absolute;left:0;right:0;top:168px;border-top:1px solid #ddd;padding:5px 7px;font-size:7.5px;color:#555;display:flex;gap:4px;align-items:center}
.plugin .sq{width:10px;height:10px}
.hot{top:467px;height:278px}
.spot{position:absolute;left:6px;right:6px;height:54px;border-bottom:1px dotted #bbb;font-size:9.5px;line-height:13.5px;color:#555}
.spot .thumb{left:1px;top:4px;width:55px;height:36px;border-width:2px}
.spot .txt{position:absolute;left:67px;top:4px}
.spot b{color:var(--link);font-weight:500;font-size:10.5px}
.more{position:absolute;right:8px;top:259px;font-size:9.5px;color:#555}
.sponsor{top:757px;height:186px}
.sponsor .thumb{left:10px;top:34px;width:190px;height:108px}
.sponsor .name{position:absolute;left:13px;top:149px;font-size:9.5px;line-height:14px}
.footer{position:absolute;left:0;top:962px;width:827px;height:238px;background:var(--footer);color:#fff}
.footer:before{content:"";position:absolute;left:0;right:0;top:0;height:17px;background:linear-gradient(#4d4d4d,var(--footer))}
.col{position:absolute;top:36px;font-size:9.5px}
.col h4{font-weight:400;font-size:13px;margin-bottom:4px;text-transform:uppercase}
.col li{list-style:none;line-height:16.6px;padding-left:15px;position:relative}
.col li:before{content:"";position:absolute;left:3px;top:5px;border-left:4px solid #fff;border-top:3px solid transparent;border-bottom:3px solid transparent}
.col.div{border-right:1px dotted #aaa;padding-right:26px;height:123px}
.cities{position:absolute;left:530px;top:45px;width:288px;font-size:9.5px;line-height:16.6px;text-align:justify}
.rule{position:absolute;left:12px;right:12px;top:192px;border-top:1px solid #999}
.copy{position:absolute;left:12px;top:207px;font-size:10px;font-family:Arial,sans-serif}
.ffollow{position:absolute;right:35px;top:205px;color:#aaa;font-size:14px;display:flex;gap:5px;align-items:center}
.ffollow .sq{background:#999}
</style>
</head>
<body>
<div class="backdrop" role="img" aria-label="Deep blue starry night backdrop with glowing light streaks"></div>
<div class="page">
  <nav class="topnav">
    <a class="tab active">Home</a><a class="tab">Order Now</a><a class="tab">FAQs</a><a class="tab">Support</a><a class="tab">Contact</a>
    <div class="account"><a>Sign Up</a>|<a>Sing in</a>|<a>Login Forgot Password?</a></div>
  </nav>
  <header class="header">
    <div class="brand">Event Ticketing</div>
    <div class="follow">Follow us on <span class="sq"></span><span class="sq alt"></span></div>
    <div class="search">-------search ticketing-------------</div>
    <div class="search-btn">Search</div>
  </header>

  <section class="panel featured">
    <div class="bar">Featured Events</div>
    <div class="frow" style="top:40px">
      <div class="thumb" role="img" aria-label="Concert crowd under blue stage lights" style="background:linear-gradient(#2f86e8,#0b3c9a)"></div>
      <div class="info">Summer at Orbit Closing Parties<br>September 3rd-5th</div>
      <div class="venue"><b>LANTERN PARADISE</b><br>Long Beach, CA</div>
      <div class="date">SATURDAY<br><span style="font-weight:400">9/3/2011</span></div>
      <div class="buy">Buy Now <i></i></div>
    </div>
    <div class="frow" style="top:117px">
      <div class="thumb" role="img" aria-label="Festival flyer with performers" style="background:linear-gradient(90deg,#6b3a24,#a8472e,#3a2a1e)"></div>
      <div class="info">Summer at Orbit Closing Parties<br>September 3rd-5th</div>
      <div class="venue"><b>LANTERN PARADISE</b><br>Long Beach, CA</div>
      <div class="date">SATURDAY<br><span style="font-weight:400">9/3/2011</span></div>
      <div class="buy">Buy Now <i></i></div>
    </div>
    <div class="frow" style="top:195px">
      <div class="thumb" role="img" aria-label="Crowd silhouettes against red stage light" style="background:radial-gradient(circle at 50% 30%,#e0452a,#5a0d08)"></div>
      <div class="info">Summer at Orbit Closing Parties<br>September 3rd-5th</div>
      <div class="venue"><b>LANTERN PARADISE</b><br>Long Beach, CA</div>
      <div class="date">SATURDAY<br><span style="font-weight:400">9/3/2011</span></div>
      <div class="buy">Buy Now <i></i></div>
    </div>
    <div class="frow" style="top:272px">
      <div class="thumb" role="img" aria-label="DJ name artwork on blue" style="background:linear-gradient(#2aa0e8,#1476c8)"></div>
      <div class="info">Summer at Orbit Closing Parties<br>September 3rd-5th</div>
      <div class="venue"><b>LANTERN PARADISE</b><br>Long Beach, CA</div>
      <div class="date">SATURDAY<br><span style="font-weight:400">9/3/2011</span></div>
      <div class="buy">Buy Now <i></i></div>
    </div>
  </section>

  <section class="panel list">
    <div class="bar">Best Sellers</div>
    <div class="item" style="top:35px"><div class="thumb" role="img" aria-label="Blue event banner" style="background:linear-gradient(#2aa0e8,#1476c8)"></div>10/6/2011<br>Special Thursday Glow@Velt -<br><span class="blue">KRAVELL Starship Tour (Live)</span><br><span class="blue">VELT NIGHTCLUB</span> | Washington, DC<div class="buy">Buy Now <i></i></div></div>
    <div class="item" style="top:114px"><div class="thumb" role="img" aria-label="Dark club banner" style="background:linear-gradient(#3a1a1a,#111)"></div>10/6/2011<br>Special Thursday Glow@Velt -<br><span class="blue">KRAVELL Starship Tour (Live)</span><br><span class="blue">VELT NIGHTCLUB</span> | Washington, DC<div class="buy">Buy Now <i></i></div></div>
    <div class="item" style="top:192px"><div class="thumb" role="img" aria-label="Purple party banner" style="background:linear-gradient(#8a7ad8,#3a2a7a)"></div>10/6/2011<br>Special Thursday Glow@Velt -<br><span class="blue">KRAVELL Starship Tour (Live)</span><br><span class="blue">VELT NIGHTCLUB</span> | Washington, DC<div class="buy">Buy Now <i></i></div></div>
  </section>

  <section class="panel list viewed">
    <div class="bar">Most Viewed Events</div>
    <div class="item" style="top:35px"><div class="thumb" role="img" aria-label="Blue event banner" style="background:linear-gradient(#2aa0e8,#1476c8)"></div>10/6/2011<br>Special Thursday Glow@Velt -<br><span class="blue">KRAVELL Starship Tour (Live)</span><br><span class="blue">VELT NIGHTCLUB</span> | Washington, DC<div class="buy">Buy Now <i></i></div></div>
    <div class="item" style="top:114px"><div class="thumb" role="img" aria-label="Dark club banner" style="background:linear-gradient(#3a1a1a,#111)"></div>10/6/2011<br>Special Thursday Glow@Velt -<br><span class="blue">KRAVELL Starship Tour (Live)</span><br><span class="blue">VELT NIGHTCLUB</span> | Washington, DC<div class="buy">Buy Now <i></i></div></div>
    <div class="item" style="top:192px"><div class="thumb" role="img" aria-label="Purple party banner" style="background:linear-gradient(#8a7ad8,#3a2a7a)"></div>10/6/2011<br>Special Thursday Glow@Velt -<br><span class="blue">KRAVELL Starship Tour (Live)</span><br><span class="blue">VELT NIGHTCLUB</span> | Washington, DC<div class="buy">Buy Now <i></i></div></div>
  </section>

  <section class="panel create">
    <div class="bar">Create Event</div>
    <svg class="arrow" style="left:6px" width="26" height="48" viewBox="0 0 26 48"><path d="M24 2 L3 24 L24 46 L20 24 Z" fill="#d6d6d6" stroke="#bbb"/></svg>
    <svg class="arrow" style="right:6px" width="26" height="48" viewBox="0 0 26 48"><path d="M2 2 L23 24 L2 46 L6 24 Z" fill="#d6d6d6" stroke="#bbb"/></svg>
    <div class="card" style="left:45px"><div class="shot" role="img" aria-label="Mountain lake under aurora" style="background:linear-gradient(#1b2f5a,#b07a4a 60%,#243a58)"></div><b>Summer at Orbit Closing</b>September 3rd-5th</div>
    <div class="card" style="left:176px"><div class="shot" role="img" aria-label="Green aurora over pine forest" style="background:linear-gradient(#0c2a3a,#2fbf6a 55%,#0a2a20)"></div><b>Summer at Orbit Closing</b>September 3rd-5th</div>
    <div class="card" style="left:307px"><div class="shot" role="img" aria-label="Glowing blue planet" style="background:radial-gradient(circle at 50% 80%,#6ad0ff,#1a5fb0 45%,#071a3a)"></div><b>Summer at Orbit Closing</b>September 3rd-5th</div>
    <div class="card" style="left:433px"><div class="shot" role="img" aria-label="Aurora over icy shore" style="background:linear-gradient(#0e2a3e,#3bc88a 45%,#6a8aa0)"></div><b>Summer at Orbit Closing</b>September 3rd-5th</div>
  </section>

  <section class="panel side login">
    <div class="sbar"><span class="ic" role="img" aria-label="Key icon" style="background:#9fb6cc;border-radius:50%"></span>Login Area</div>
    <div class="field" style="top:52px">username :<span></span></div>
    <div class="field" style="top:74px">Password :<span></span></div>
    <div class="login-btn">Login</div>
    <div class="forgot">Forgot your password?</div>
  </section>

  <section class="panel side fb">
    <div class="sbar"><span class="sq" style="background:#3b5a9a;border:1px solid #fff"></span>Follow Brookline</div>
    <div class="like">Like</div>
    <div class="fbname">Brookline</div>
    <div class="fbcount">1,234 Peopel like lanternfold.example</div>
    <div class="faces" role="img" aria-label="Grid of eight fan profile photos">
      <span style="background:#c9a48a"></span><span style="background:#8a5a44"></span><span style="background:#7aa6c8"></span><span style="background:#b89a6a"></span>
      <span style="background:#c68a4a"></span><span style="background:#a07060"></span><span style="background:linear-gradient(90deg,#c33,#e9c23a,#3a8a3a,#3050c0)"></span><span style="background:#9a7a5a"></span>
    </div>
    <div class="plugin"><span class="sq" style="background:#3b5a9a"></span>Brookline social plugin</div>
  </section>

  <section class="panel side hot">
    <div class="sbar"><svg class="ic" viewBox="0 0 22 20"><circle cx="11" cy="9" r="2" fill="#fff"/><path d="M11 11 L8 19 M11 11 L14 19" stroke="#fff"/><path d="M6 4 a7 7 0 0 0 0 10 M16 4 a7 7 0 0 1 0 10 M3 1 a11 11 0 0 0 0 16 M19 1 a11 11 0 0 1 0 16" stroke="#fff" fill="none"/></svg>Local hotspots</div>
    <div class="spot" style="top:36px"><div class="thumb" role="img" aria-label="Venue exterior" style="background:linear-gradient(#9ab0c8,#4a5a6a)"></div><div class="txt"><b>Harbor Hall Los Angeles</b><br>8412 West Palmer<br>Boulevard</div></div>
    <div class="spot" style="top:96px;height:50px"><div class="thumb" role="img" aria-label="Theatre interior" style="background:linear-gradient(#6a8ab0,#222)"></div><div class="txt" style="left:70px;top:6px"><b>The Corvane Theatre</b><br>3750 Ormond Boulevard</div></div>
    <div class="spot" style="top:155px"><div class="thumb" role="img" aria-label="Club stage lit in blue and red" style="background:linear-gradient(#2a3aa0,#c03a6a)"></div><div class="txt"><b>Harbor Hall Los Angeles</b><br>8412 West Palmer<br>Boulevard</div></div>
    <div class="spot" style="top:211px;border:none"><div class="thumb" role="img" aria-label="Flyer with bird on branch" style="background:linear-gradient(#d8ccb8,#6a5a4a)"></div><div class="txt" style="left:70px;top:6px"><b>The Corvane Theatre</b><br>3750 Ormond Boulevard</div></div>
    <div class="more">See more <span style="color:var(--link)">&#9656;</span></div>
  </section>

  <section class="panel side sponsor">
    <div class="sbar"><span class="ic" role="img" aria-label="Trophy icon" style="background:#c8a86a;border-radius:4px"></span>SPONSORED BY</div>
    <div class="thumb" role="img" aria-label="Bowling alley lanes" style="background:linear-gradient(#b85a3a 0 22%,#c8b49a 22%,#e8d8c0)"></div>
    <div class="name"><span class="blue">Mira's Pub</span><br>418 Delmore Street New York, NY</div>
  </section>

  <footer class="footer">
    <div class="col div" style="left:12px">
      <h4>About Eventticketing</h4>
      <ul><li>About Us</li><li>Contact Us</li><li>Jobs</li><li>Pricing</li><li>Referral Program</li><li>Press</li></ul>
    </div>
    <div class="col div" style="left:205px;height:140px">
      <h4>Policies</h4>
      <ul><li>Concerts &amp; Tour Dates</li><li>Festivals</li><li>Kids &amp; Family Events</li><li>Singles Events</li><li>Fundraisers</li><li>Food Events</li><li>Performing Arts</li></ul>
    </div>
    <div class="col div" style="left:360px;height:140px">
      <h4>How to advertise</h4>
      <ul><li>Sell Tickets Online</li><li>Free Online Event Registration</li><li>Promote Events Online</li><li>Collect Donations Online</li><li>Send Email Invitations</li><li>Publish Event to Brookline</li></ul>
    </div>
    <div class="cities">Cities Atlanta, Austin, Boston, Chicago, Denver, Houston, London, Los Angeles, Miami, New York City, Philadelphia, San Francisco, San Jose, Seattle, Toronto, Vancouver, Washington DC<br><br>Popular Searches Tollaquin At the Door, Event Management, Labor Day, NYC Events, Tablet, Conferences in New York, London Events, Organizing Community Events, Online Event Registration,</div>
    <div class="rule"></div>
    <div class="copy">© 2011 Eventticketing. All Rights Reserved. Terms of Service. Privacy Policy.</div>
    <div class="ffollow">Follow us on <span class="sq"></span><span class="sq"></span></div>
  </footer>
</div>
</body>
</html>
```